Webseite Toilettenvermietung
Zielgruppe
Wir vermieten mobile Toilettenkabine und Toilettenwagen. Wir haben noch eine Webseite kabinenpark-nord.de und lokus-verleihhaus.de und benötigen noch eine weitere. Es sollen nur die Miettoiletten und Toilettenwagen beworben werden
Aufgabenstellung
saubere und aussageräftige, farbliches Erscheinungsbild der Startseite.

```html
<!DOCTYPE html>
<html lang="de">
<head>
<meta charset="utf-8">
<title>KLARO MOBIL – WC Mietservice</title>
<link href="https://fonts.googleapis.com/css2?family=Roboto:wght@300;400;500&display=swap" rel="stylesheet">
<style>
:root{
  --blue:#1a62b4;
  --blue-dark:#0f4f99;
  --green:#8cbc16;
  --text:#333;
  --muted:#8a8a8a;
  --line:#e3e3e3;
  --page:#f2f2f2;
  --panel:#fff;
  --soft:#f8f8f8;
}
*{margin:0;padding:0;box-sizing:border-box}
html,body{width:1200px;height:1106px;overflow:hidden}
body{background:var(--page);font-family:'Roboto',sans-serif;font-weight:300;color:var(--text);position:relative}
.topbar{position:absolute;left:0;top:0;width:1200px;height:44px;background:#fff;border-bottom:1px solid #d8d8d8}
.brand{position:absolute;left:300px;top:10px;display:flex;align-items:center;gap:6px;font-weight:500;font-size:17px;color:var(--blue);letter-spacing:.5px}
.brand-dot{width:16px;height:16px;border-radius:50%;background:var(--blue)}
.nav{position:absolute;left:579px;top:0;display:flex;height:44px;font-size:10.5px;font-weight:400;color:#555}
.nav a{display:flex;align-items:center;padding:0 12px;text-decoration:none;color:inherit}
.nav a.active{background:var(--blue);color:#fff}
.search{position:absolute;left:889px;top:17px}
.sheet{position:absolute;left:300px;top:44px;width:600px;height:1034px;background:var(--panel)}
.hero{position:absolute;left:0;top:0;width:600px;height:281px;background:radial-gradient(circle at 70% 40%,#6a4aa0 0%,#3a2a78 35%,#1a1640 75%,#120f2a 100%)}
.hero-box{position:absolute;left:22px;top:64px;width:295px;height:144px;background:rgba(10,10,20,.72);border-radius:4px}
.hero-title{position:absolute;left:15px;top:12px;font-size:33px;font-weight:400;color:var(--blue)}
.hero-text{position:absolute;left:17px;top:53px;width:230px;font-size:8.6px;line-height:10.5px;color:#ddd}
.btn{display:flex;align-items:center;justify-content:center;background:var(--green);color:#fff;font-weight:400;text-decoration:none}
.hero-btn{position:absolute;left:17px;top:96px;width:125px;height:25px;font-size:11px}
.dots{position:absolute;left:566px;top:270px;display:flex;gap:3px}
.dots i{width:6px;height:6px;border-radius:50%;background:rgba(255,255,255,.6)}
.dots i:first-child{background:#fff}
.welcome{position:absolute;left:30px;top:302px;width:540px;text-align:center;font-size:19px;line-height:22.5px;color:var(--blue);text-transform:uppercase}
.rule{position:absolute;left:8px;top:367px;width:584px;height:1px;background:linear-gradient(90deg,transparent,#ddd 20%,#ddd 80%,transparent)}
.card{position:absolute;top:398px;width:156px;height:194px;border:1px solid var(--line);border-top:2px solid var(--blue);text-align:center}
.card svg{position:absolute;left:48px;top:16px}
.card h3{position:absolute;top:93px;width:100%;font-size:14px;font-weight:400;color:#333}
.card p{position:absolute;top:115px;left:14px;right:14px;font-size:8.8px;line-height:15px;color:var(--muted)}
.card a{position:absolute;top:164px;left:0;width:100%;font-size:9px;font-weight:400;color:var(--blue);text-decoration:none}
.info{position:absolute;left:0;top:624px;width:600px;height:213px;background:var(--soft);border-top:1px solid #e6e6e6;border-bottom:1px solid #e6e6e6}
.info h2{font-size:20px;font-weight:300;color:#444}
.about{position:absolute;left:37px;top:14px;width:320px}
.info p{margin-top:12px;font-size:8.6px;line-height:13.75px;color:var(--muted)}
.divider{position:absolute;left:384px;top:22px;width:1px;height:166px;background:#e2e2e2}
.news{position:absolute;left:406px;top:14px;width:155px}
.news-btn{position:absolute;left:472px;top:173px;width:87px;height:22px;font-size:8.6px}
.products-title{position:absolute;top:858px;width:600px;text-align:center;font-size:15px;font-weight:300;color:var(--blue)}
.product{position:absolute;top:887px;text-align:center;font-size:9.8px;line-height:12px;color:#999;text-transform:uppercase}
.product.active{color:var(--blue)}
.product .shot{margin:0 auto 16px;height:88px}
.footer{position:absolute;left:305px;top:1087px;display:flex;gap:9px;font-size:8.8px;font-weight:400;color:#888}
</style>
</head>
<body>
<header class="topbar">
  <div class="brand"><span class="brand-dot"></span>KLARO MOBIL</div>
  <nav class="nav">
    <a class="active">Startseite</a><a>Miettoiletten</a><a>Toilettenwagen</a><a>Kontakt</a>
  </nav>
  <svg class="search" width="10" height="10" viewBox="0 0 10 10" fill="none" stroke="#333" stroke-width="1.2"><circle cx="4.2" cy="4.2" r="3.2"/><path d="M6.6 6.6L9.3 9.3"/></svg>
</header>

<main class="sheet">
  <section class="hero" role="img" aria-label="Konzertpublikum mit erhobenen Händen vor einer beleuchteten Bühne">
    <div class="hero-box">
      <div class="hero-title">KOMMSTE MIT?</div>
      <p class="hero-text">Lorem Ipsum is simply dummy text of the printing and typesetting industry. Lorem Ipsum has been the industry's standard dummy text ever since the 1500s....</p>
      <a class="btn hero-btn">CONTACT US</a>
    </div>
    <div class="dots"><i></i><i></i><i></i></div>
  </section>

  <h1 class="welcome">Willkommen bei KLARO MOBIL, Ihr WC Mietservice für mobile WC Kabinen, Wagen &amp; Container</h1>
  <div class="rule"></div>

  <article class="card" style="left:37px">
    <svg width="60" height="60" viewBox="0 0 60 60"><circle cx="30" cy="30" r="29.5" fill="var(--blue)"/><g fill="none" stroke="#fff" stroke-width="2" stroke-linecap="round"><path d="M40 17L31 28"/><path d="M24 27l10 5-4 9-11-4c3-2 4-6 5-10z"/><path d="M22 36l-3 3M26 38l-2 4"/></g><circle cx="37" cy="40" r="1.3" fill="#fff"/><circle cx="40" cy="43" r="1.3" fill="#fff"/></svg>
    <h3>Clean</h3>
    <p>Lorem Ipsum is simply dummy text of the printing and typesetting industry.</p>
    <a>Read More</a>
  </article>
  <article class="card" style="left:222px">
    <svg width="60" height="60" viewBox="0 0 60 60"><circle cx="30" cy="30" r="29" fill="#fff" stroke="var(--blue)" stroke-width="1"/><g fill="var(--blue)"><rect x="12" y="18" width="23" height="18" rx="1.5"/><path d="M36 24h7l5 6v6H36z"/><circle cx="19" cy="38" r="4"/><circle cx="42" cy="38" r="4"/></g><circle cx="19" cy="38" r="1.6" fill="#fff"/><circle cx="42" cy="38" r="1.6" fill="#fff"/></svg>
    <h3>Transport</h3>
    <p>Lorem Ipsum is simply dummy text of the printing and typesetting industry.</p>
    <a>Read More</a>
  </article>
  <article class="card" style="left:407px">
    <svg width="60" height="60" viewBox="0 0 60 60"><circle cx="30" cy="30" r="29" fill="#fff" stroke="var(--blue)" stroke-width="1"/><g stroke="var(--blue)" stroke-linecap="round"><path d="M20 40L40 20" stroke-width="4"/><path d="M22 20l18 20" stroke-width="4"/></g><circle cx="41" cy="19" r="5" fill="none" stroke="var(--blue)" stroke-width="3"/><rect x="17" y="16" width="6" height="6" fill="var(--blue)"/></svg>
    <h3>Installation</h3>
    <p>Lorem Ipsum is simply dummy text of the printing and typesetting industry.</p>
    <a>Read More</a>
  </article>

  <section class="info">
    <div class="about">
      <h2>About KLARO MOBIL</h2>
      <p>Lorem Ipsum is simply dummy text of the printing and typesetting industry. Lorem Ipsum has been the industry's standard dummy text ever since the 1500s, when an unknown printer took a galley of type and scrambled it to make a type specimen book.<br>It has survived not only five centuries, but also the leap into electronic typesetting, remaining essentially unchanged.<br>It was popularised in the 1960s with the release of Letraset sheets containing Lorem Ipsum passages, and more recently with desktop publishing software like Aldus PageMaker including versions of Lorem Ipsum.</p>
    </div>
    <div class="divider"></div>
    <div class="news">
      <h2>News</h2>
      <p>Lorem Ipsum is simply dummy text of the printing and typesetting industry. Lorem Ipsum has been the industry's standard dummy text ever since the 1500s, when an unknown printer took a galley of type and scrambled it to make a type specimen book. It has survived not only five centuries.</p>
    </div>
    <a class="btn news-btn">More News</a>
  </section>

  <h2 class="products-title">Products</h2>
  <div class="product active" style="left:35px;width:102px">
    <div class="shot" role="img" aria-label="Blaue mobile WC-Kabine" style="width:30px;background:linear-gradient(90deg,#1a5fb8,#3f8ee0,#1a5fb8);border-radius:6px 6px 2px 2px"></div>
    Mobile WC Kabinen<br>mieten
  </div>
  <div class="product" style="left:164px;width:115px">
    <div class="shot" role="img" aria-label="WC-Container mit mehreren Türen" style="width:110px;height:70px;margin-top:10px;margin-bottom:24px;background:linear-gradient(90deg,#9a9ea3 40%,#e7e9ec 40%);border:4px solid #2b2f7a"></div>
    Mobile WC Container<br>mieten
  </div>
  <div class="product" style="left:297px;width:108px">
    <div class="shot" role="img" aria-label="Graue mobile WC-Anlage" style="width:34px;background:linear-gradient(90deg,#6f7377,#a3a7ab,#6f7377);border-radius:6px 6px 2px 2px"></div>
    Mobile WC Anlagen<br>kaufen
  </div>
  <div class="product" style="left:416px;width:145px">
    <div class="shot" role="img" aria-label="Weißer Toilettenwagen mit zwei Eingängen und Treppen" style="width:146px;height:72px;margin-top:12px;margin-bottom:20px;background:linear-gradient(180deg,#f4f5f7 0 80%,#2e3a9a 80%);border:1px solid #c9ccd2"></div>
    Mobile WC Wagen<br>mieten
  </div>
</main>

<footer class="footer"><span>Produkte</span><span>News &amp; Infos</span><span>Unternehmen</span><span>Kontakt</span><span>AGB</span><span>Impressum</span></footer>
</body>
</html>
```